Simple, elegant, business card design required

Hi designers,I am looking for a simple yet elegant business card design.

Please make use of my logo (attached); you are free to tweak the logo should you wish to do so.

Our business is involved in many different fields - almost all of them involved in some form of "design", so that's really one of the key things I want to portray. I do not wish to specify which field of design, exactly.

I prefer white on black (or just monochromatic), but if you have a different, creative idea, I am open to that too.

You can use artsy photographs provided that you have the license to use those. Please feel free to ask me any questions.
Updates

Project Deadline Extended Reason: Small extension for potential revisions. Did not get the time to provide as much feedback as I can. Added Wednesday, July 09, 2014

Target Market(s)

High-end customers looking for design consultancy

Industry/Entity Type

Business

Contact Information for Business Card

Name: Gareth Moonfield
Position: Creative Director
Mobile: +155603928174
Address: Barrow Lane, Ashcombe upon Tarn, Wexmoorshire GL12 4RT
Website: torvakest.com (not launched yet)

Requirements
Must have
• Design layout must be clean, original, and text must be readable when printed.
Should not have
• ~ No business card templates please. Anyone using this will be reported.
• ~ Please don't spam entries.

```html
<!DOCTYPE html>
<html lang="en">
<head>
<meta charset="utf-8">
<title>Torvakest – Business Card</title>
<link rel="stylesheet" href="https://fonts.googleapis.com/css2?family=Open+Sans:wght@400&family=Oswald:wght@300&display=swap">
<style>
  :root {
    --backdrop: #898989;
    --card: #ffffff;
    --ink: #111111;
    --ink-soft: #555555;
    --block: #231f20;
    --rule: #333333;
  }
  * { margin: 0; padding: 0; box-sizing: border-box; }
  html, body {
    width: 1200px;
    height: 900px;
    overflow: hidden;
    background: var(--backdrop);
  }
  .card {
    position: absolute;
    left: 100px;
    top: 157px;
    width: 997px;
    height: 584px;
    background: var(--card);
    font-family: "Open Sans", sans-serif;
    color: var(--ink);
  }
  .brand-name {
    position: absolute;
    left: 147px;
    top: 249px;
    transform: translate(-50%, -50%) rotate(-90deg);
    font-family: "Oswald", sans-serif;
    font-weight: 300;
    font-size: 44px;
    letter-spacing: 11px;
    line-height: 1;
    color: var(--ink);
    white-space: nowrap;
  }
  .brand-block {
    position: absolute;
    left: 72px;
    bottom: 0;
    width: 158px;
    height: 168px;
    background: var(--block);
  }
  .divider {
    position: absolute;
    left: 414px;
    top: 142px;
    height: 300px;
    border-left: 2px dotted var(--rule);
  }
  .details {
    position: absolute;
    right: 76px;
    top: 0;
    text-align: right;
    line-height: 1;
    white-space: nowrap;
  }
  .details > * { position: absolute; right: 0; font-weight: 400; }
  .person-name { top: 50px; font-size: 51px; }
  .person-name .surname { color: var(--ink-soft); }
  .person-role { top: 122px; font-size: 28px; color: var(--ink-soft); }
  .label { font-size: 33px; }
  .value { font-size: 21px; letter-spacing: 0.6px; line-height: 28.5px; }
  .mobile-label { top: 184px; }
  .mobile-value { top: 230px; }
  .address-label { top: 283px; }
  .address-value { top: 325px; }
  .website-label { top: 403px; }
  .website-value { top: 439px; }
</style>
</head>
<body>
  <main class="card">
    <div class="brand-name">TORVAKEST</div>
    <div class="brand-block"></div>
    <div class="divider"></div>
    <section class="details">
      <h1 class="person-name">Gareth <span class="surname">Moonfield</span></h1>
      <p class="person-role">Creative Director</p>
      <h2 class="label mobile-label">Mobile</h2>
      <p class="value mobile-value">+155603928174</p>
      <h2 class="label address-label">Address</h2>
      <p class="value address-value">Barrow Lane, Ashcombe upon Tarn,<br>Wexmoorshire GL12 4RT</p>
      <h2 class="label website-label">Website</h2>
      <p class="value website-value">torvakest.com</p>
    </section>
  </main>
</body>
</html>
```